Design Emoji directory website with a modern look

Please design the Emoji directory website to display a nice search box as well as design a nice search suggestion dropdown page. Example when you type keyword in Brindlo.
You can use Emojis in SVG file https://www.filvex.com/s/8kq2207p5mzwtna/svg.rar?dl=0 to create designs.
The following are 7 example pages but please make sure the design is UNIQUE.
Main page example
https://glyphora.info/
Content page example
https://glyphora.info/smiling-face-with-smiling-eyes/
Category page example
https://glyphora.info/smileys-and-emotion-category/
Holiday page example
https://glyphora.info/holidays/
Static pages example
https://glyphora.info/privacy-policy/
404 page not found example
https://glyphora.info/category/
Search page example
https://glyphora.info/?s=exchange+rate
Target Market(s)
web design
Industry/Entity Type
Website
Number of Pages Required
5+ page
Font styles to use
Other font styles liked:
- COMIC NEUE
Colors
Designer to choose colors to be used in the design.
Requirements
Must have
- Please make sure its unique, modern look, clean.
Should not have
- Do not use heavy graphics, we only use CSS style rules and SVG's emojis to make sure the site loads fast.

```html
<!DOCTYPE html>
<html lang="en">
<head>
<meta charset="utf-8">
<title>Painter Face With Palette Emoji</title>
<link rel="stylesheet" href="https://fonts.googleapis.com/css2?family=Inter:wght@300;400;500;600;700&display=swap">
<style>
:root{
  --pink:#d10a67;
  --pink-soft:#f07aa3;
  --header:#ee7d9f;
  --footer:#db4a76;
  --footer-dark:#c9355f;
  --ink:#111;
  --muted:#555;
  --line:#e6e6e6;
  --glyph:#f7c23a;
}
*{box-sizing:border-box;margin:0;padding:0}
html,body{width:1200px;height:4345px;overflow:hidden}
body{position:relative;background:#fff;font-family:"Inter",sans-serif;color:var(--ink)}
.abs{position:absolute}
.accent{color:var(--pink)}
.glyph{display:inline-block;width:22px;height:22px;border-radius:50%;background:var(--glyph);vertical-align:middle}
.glyph.sm{width:18px;height:18px}
.glyph.lg{width:54px;height:54px}
.glyph.tone{background:linear-gradient(135deg,#f2c08a,#7b8fa6)}

/* header */
.site-header{left:0;top:0;width:1200px;height:169px;background:linear-gradient(90deg,#f58bab,#ec6f95 50%,#f58bab)}
.site-header .art{position:absolute;border-radius:50%;background:rgba(255,170,80,.55)}
.logo{left:225px;top:33px;color:#fff;font-weight:600;font-size:21px}
.main-nav{left:617px;top:35px;display:flex;gap:24px;color:#fff;font-size:15px;font-weight:500}
.main-nav span.active{border-bottom:2px solid #fff;padding-bottom:12px}
.search{left:322px;top:100px;width:556px;height:42px;background:#fff;border-radius:6px;display:flex;align-items:center;padding-left:22px;font-size:14px;color:#333}
.search i{width:24px;height:24px;border-radius:50%;background:var(--pink-soft);margin-right:14px;position:relative}
.search i:after{content:"";position:absolute;left:7px;top:6px;width:8px;height:8px;border:2px solid #fff;border-radius:50%}

/* category strip */
.cat-strip{left:0;top:169px;width:1200px;height:79px;border-bottom:3px solid #eee;background:#fff}
.cat{position:absolute;top:14px;width:90px;margin-left:-45px;text-align:center;font-size:11px;color:#333}
.cat .ico{display:block;width:28px;height:28px;margin:0 auto 8px;border-radius:8px;background:#e9e3df}
.arrow{position:absolute;top:30px;color:#888;font-size:18px}

/* content */
h1.page-title{left:225px;top:300px;font-size:44px;font-weight:700;display:flex;align-items:center;gap:18px;letter-spacing:-.5px}
h2.sec{position:absolute;left:225px;font-size:24px;font-weight:600;display:flex;align-items:center;gap:12px;white-space:nowrap}
p.body{position:absolute;left:225px;width:650px;font-size:14px;line-height:25px;color:#444;font-weight:300}
.hint{position:absolute;left:225px;font-size:11px;color:#666}

.tap{left:484px;top:846px;width:230px;height:59px;border-radius:6px;border:2px solid var(--pink);display:flex;overflow:hidden}
.tap .lbl{flex:1;background:var(--pink);color:#fff;font-size:16px;display:flex;align-items:center;justify-content:center}
.tap .pic{width:74px;display:flex;align-items:center;justify-content:center}

.bullets{left:225px;top:1006px;list-style:disc;padding-left:18px;font-size:15px;line-height:25px;color:#333;font-weight:300}
.bullets li{text-decoration:underline;text-decoration-color:#bbb}

.chip{position:absolute;width:236px;height:52px;border-radius:4px;box-shadow:0 2px 10px rgba(0,0,0,.12);display:flex;background:#fff;overflow:hidden}
.chip .t{flex:1;display:flex;align-items:center;gap:12px;padding-left:18px;font-size:15px;font-weight:600}
.chip .cp{width:50px;background:var(--pink);display:flex;align-items:center;justify-content:center}
.cp svg{width:20px;height:20px}
.chip.add{background:var(--pink);color:#fff;justify-content:center;align-items:center;font-size:16px;font-weight:600;gap:10px}

.combo{position:absolute;width:172px;height:53px;border-radius:4px;box-shadow:0 2px 10px rgba(0,0,0,.12);display:flex;background:#fff;overflow:hidden}
.combo .t{flex:1;display:flex;align-items:center;justify-content:center;gap:14px}
.combo .cp{width:50px;background:var(--pink);display:flex;align-items:center;justify-content:center}
.combo.add{background:var(--pink);color:#fff;justify-content:center;align-items:center;font-weight:600;font-size:16px;gap:10px}
.combo-cap{position:absolute;width:172px;text-align:center;font-size:15px;color:#444;font-weight:300}

.card{position:absolute;width:168px;height:169px;border-radius:6px;box-shadow:0 2px 12px rgba(0,0,0,.1);background:#fff;text-align:center;padding-top:42px;font-size:17px;color:#444;font-weight:300}
.card .glyph{display:block;margin:0 auto 22px}
.card.on{background:var(--pink);color:#fff;font-weight:400}

/* info table */
.info{left:225px;top:2821px;width:732px;height:518px;border:3px solid var(--pink);border-radius:14px;overflow:hidden;display:flex}
.info .k{width:298px;background:var(--pink);color:#fff;font-size:15px;font-weight:600;padding:28px 0 0 63px}
.info .v{flex:1;padding:28px 0 0 45px;font-size:15px;color:#333;font-weight:500}
.info .row{height:53px;display:flex;align-items:flex-start;gap:10px}
.code{display:inline-flex;align-items:center;gap:22px;background:#e4e4e4;padding:8px 22px;border-radius:3px;color:#444;margin-top:-10px}

.trans{left:225px;top:3457px;width:732px;height:572px;border:3px solid var(--pink);border-radius:22px}
.trans .div{position:absolute;left:302px;top:50px;width:1px;height:470px;background:#ccc}
.trans .k{position:absolute;left:57px;font-size:15px;font-weight:600}
.trans .v{position:absolute;left:365px;font-size:15px;font-weight:600;color:#444}
.trans .kw{position:absolute;left:365px;font-size:15px;font-weight:600;color:#444;display:flex;align-items:center;gap:10px}

/* footer */
.site-footer{left:0;top:4137px;width:1200px;height:208px;background:var(--footer);border-radius:22px 22px 0 0;color:#fff;text-align:center}
.site-footer .flogo{margin-top:56px;font-size:22px;font-weight:700}
.site-footer .tag{margin-top:8px;font-size:11px}
.social{display:flex;justify-content:center;gap:12px;margin-top:14px}
.social span{width:30px;height:30px;border:1.5px solid #fff;border-radius:50%}
.bottom{position:absolute;left:0;bottom:0;width:100%;height:32px;background:var(--footer-dark);font-size:11px;line-height:32px;color:#fde}
</style>
</head>
<body>

<header class="abs site-header" role="img" aria-label="Pink header with large soft emoji illustrations">
  <span class="art" style="left:-20px;top:-20px;width:130px;height:110px"></span>
  <span class="art" style="left:440px;top:-30px;width:140px;height:130px"></span>
  <span class="art" style="left:860px;top:60px;width:200px;height:150px"></span>
  <span class="art" style="left:1050px;top:-40px;width:130px;height:110px"></span>
  <span class="art" style="left:160px;top:80px;width:130px;height:110px;background:rgba(230,40,60,.6)"></span>
</header>
<div class="abs logo">LOGO</div>
<nav class="abs main-nav"><span class="active">People</span><span>Emoticon</span><span>Nature</span><span>Animals</span><span>Life</span></nav>
<div class="abs search"><i></i>Painter Face</div>

<div class="abs cat-strip">
  <span class="arrow" style="left:222px">‹</span>
  <div class="cat" style="left:270px"><span class="ico" role="img" aria-label="guitar icon"></span>Music</div>
  <div class="cat" style="left:368px"><span class="ico" role="img" aria-label="health icon"></span>Health</div>
  <div class="cat" style="left:461px"><span class="ico" role="img" aria-label="flag icon"></span>Flags</div>
  <div class="cat" style="left:552px"><span class="ico" role="img" aria-label="monument icon"></span>Monuments</div>
  <div class="cat" style="left:646px"><span class="ico" role="img" aria-label="orange icon"></span>Fruits</div>
  <div class="cat" style="left:738px"><span class="ico" role="img" aria-label="snowman icon"></span>Seasons</div>
  <div class="cat" style="left:830px"><span class="ico" role="img" aria-label="wedding icon"></span>Wedding</div>
  <div class="cat" style="left:923px"><span class="ico" role="img" aria-label="worker icon"></span>Work</div>
  <span class="arrow" style="left:966px">›</span>
</div>

<h1 class="abs page-title"><span class="glyph tone" style="width:40px;height:40px" role="img" aria-label="painter emoji"></span><span>Painter Face With Palette <span class="accent">Emoji</span></span></h1>

<h2 class="sec" style="top:398px"><span class="glyph" role="img" aria-label="emoji"></span>Meaning of <span class="glyph tone sm" role="img" aria-label="painter emoji"></span> Painter Face With Palette Emoji</h2>
<p class="body" style="top:449px">Lorem ipsum dolor sit amet, consectetur adipiscing elit, sed do eiusmod tempor incididunt ut labore et dolore magna aliqua. Ut enim ad minim veniam, quis nostrud exercitation ullamco laboris nisi ut aliquip ex ea commodo consequat. Duis aute irure dolor in reprehenderit in voluptate velit esse cillum dolore eu fugiat nulla pariatur. Excepteur sint occaecat cupidatat non proident, sunt in culpa qui officia deserunt mollit anim id est laborum</p>

<h2 class="sec" style="top:618px"><span class="glyph" role="img" aria-label="emoji"></span>ChatLine Meaning <span class="glyph tone sm" role="img" aria-label="painter emoji"></span>&nbsp;&nbsp;&nbsp;Painter Face With <span class="accent">Palette Emoji</span></h2>
<p class="body" style="top:673px">Lorem ipsum dolor sit amet, consectetur adipiscing elit, sed do eiusmod tempor incididunt ut labore et dolore magna aliqua. Ut enim ad minim veniam, quis nostrud exercitation ullamco laboris nisi ut aliquip ex ea commodo consequat. Duis aute irure dolor in reprehenderit in voluptate velit esse cillum dolore eu fugiat nulla pariatur. Excepteur sint occaecat cupidatat non proident, sunt in culpa qui officia deserunt mollit anim id est laborum</p>

<div class="abs tap"><span class="lbl">Tap to Copy &nbsp;››</span><span class="pic"><span class="glyph tone" style="width:36px;height:36px" role="img" aria-label="painter emoji"></span></span></div>

<h2 class="sec" style="top:951px"><span class="glyph tone" role="img" aria-label="emoji"></span>Other Categories You Want To <span class="accent">Check Out</span></h2>
<ul class="abs bullets">
  <li>Lorem ipsum <span class="glyph sm" role="img" aria-label="emoji"></span> dolor sit amet</li>
  <li>labore <span class="glyph sm" role="img" aria-label="emoji"></span> et dolore magna aliqua.</li>
  <li>laboris nisi ut aliquip ex <span class="glyph sm" role="img" aria-label="emoji"></span> ea</li>
  <li>voluptate <span class="glyph sm" role="img" aria-label="emoji"></span> velit esseprovident.</li>
  <li>sunt in culpa <span class="glyph sm" role="img" aria-label="emoji"></span> qui officia deserunt</li>
</ul>

<h2 class="sec" style="top:1173px"><span class="glyph tone" role="img" aria-label="emoji"></span>Examples of Smiley Emoji With Thoughts!</h2>
<div class="hint" style="top:1223px">Tap to Copy / Paste</div>

<svg width="0" height="0" style="position:absolute"><defs><g id="copy"><rect x="5" y="2" width="11" height="14" rx="1.5" fill="none" stroke="#fff" stroke-width="1.6"/><rect x="2" y="5" width="11" height="14" rx="1.5" fill="#d10a67" stroke="#fff" stroke-width="1.6"/><path d="M5 9h5M5 12h5M5 15h5" stroke="#fff" stroke-width="1.4"/></g></defs></svg>

<div class="chip" style="left:225px;top:1258px"><span class="t"><span class="glyph sm" role="img" aria-label="chick emoji"></span>Chicks are cute</span><span class="cp"><svg viewBox="0 0 20 20"><use href="#copy"/></svg></span></div>
<div class="chip" style="left:481px;top:1258px"><span class="t"><span class="glyph sm" style="background:#333" role="img" aria-label="game controller emoji"></span>I Love Games</span><span class="cp"><svg viewBox="0 0 20 20"><use href="#copy"/></svg></span></div>
<div class="chip" style="left:738px;top:1258px"><span class="t"><span class="glyph sm" role="img" aria-label="smiley emoji"></span>Life's is happy</span><span class="cp"><svg viewBox="0 0 20 20"><use href="#copy"/></svg></span></div>
<div class="chip" style="left:225px;top:1342px"><span class="t"><span class="glyph sm" role="img" aria-label="sorry emoji"></span>I am Sorry</span><span class="cp"><svg viewBox="0 0 20 20"><use href="#copy"/></svg></span></div>
<div class="chip" style="left:481px;top:1342px"><span class="t"><span class="glyph sm tone" role="img" aria-label="person emoji"></span>Talk with people</span><span class="cp"><svg viewBox="0 0 20 20"><use href="#copy"/></svg></span></div>
<div class="chip add" style="left:738px;top:1342px"><span style="font-size:22px;font-weight:300">+</span>Add New</div>

<h2 class="sec" style="top:1442px"><span class="glyph tone" role="img" aria-label="emoji"></span>Combination Emoji of Smiley <span class="glyph" role="img" aria-label="smiley emoji"></span> and <span class="accent">Chick</span> <span class="glyph sm" role="img" aria-label="chick emoji"></span></h2>
<div class="hint" style="top:1490px">Tap to Copy / Paste</div>

<div class="combo" style="left:225px;top:1524px"><span class="t"><span class="glyph" role="img" aria-label="smiley emoji"></span><span class="glyph" style="background:#fbb34c" role="img" aria-label="chick emoji"></span></span><span class="cp"><svg viewBox="0 0 20 20"><use href="#copy"/></svg></span></div>
<div class="combo" style="left:422px;top:1524px"><span class="t"><span class="glyph" role="img" aria-label="smiley emoji"></span><span class="glyph" style="background:#9bb8d6" role="img" aria-label="building emoji"></span></span><span class="cp"><svg viewBox="0 0 20 20"><use href="#copy"/></svg></span></div>
<div class="combo" style="left:627px;top:1524px"><span class="t"><span class="glyph" role="img" aria-label="smiley emoji"></span><span class="glyph" style="background:#333" role="img" aria-label="game controller emoji"></span></span><span class="cp"><svg viewBox="0 0 20 20"><use href="#copy"/></svg></span></div>
<div class="combo-cap" style="left:225px;top:1586px">Lorem ipsum</div>
<div class="combo-cap" style="left:422px;top:1586px">Lorem ipsum</div>
<div class="combo-cap" style="left:627px;top:1586px">Lorem ipsum</div>
<div class="combo" style="left:225px;top:1632px"><span class="t"><span class="glyph" role="img" aria-label="smiley emoji"></span><span class="glyph" style="background:#fbb34c" role="img" aria-label="chick emoji"></span></span><span class="cp"><svg viewBox="0 0 20 20"><use href="#copy"/></svg></span></div>
<div class="combo" style="left:422px;top:1632px"><span class="t"><span class="glyph" role="img" aria-label="smiley emoji"></span><span class="glyph" style="background:#9bb8d6" role="img" aria-label="building emoji"></span></span><span class="cp"><svg viewBox="0 0 20 20"><use href="#copy"/></svg></span></div>
<div class="combo add" style="left:627px;top:1632px"><span style="font-size:22px;font-weight:300">+</span>Add New</div>
<div class="combo-cap" style="left:225px;top:1694px">Lorem ipsum</div>
<div class="combo-cap" style="left:422px;top:1694px">Lorem ipsum</div>
<div class="combo-cap" style="left:627px;top:1694px">Got Your Own Idea ?</div>

<p class="body" style="top:1728px">Lorem ipsum dolor sit amet, consectetur adipiscing elit, sed do eiusmod tempor incididunt ut labore et dolore magna aliqua. Ut enim ad minim veniam, quis nostrud exercitation ullamco laboris nisi ut aliquip ex ea commodo consequat. Duis aute irure dolor in reprehenderit in voluptate velit esse cillum dolore eu fugiat nulla pariatur. Excepteur sint occaecat cupidatat non proident, sunt in culpa qui officia deserunt mollit anim id est laborum</p>

<h2 class="sec" style="top:1899px"><span class="glyph tone" role="img" aria-label="emoji"></span>Related <span class="accent">Emoji</span></h2>
<div class="card" style="left:225px;top:1961px"><span class="glyph lg" role="img" aria-label="grimacing emoji"></span>Oops Emoji</div>
<div class="card" style="left:419px;top:1961px"><span class="glyph lg" role="img" aria-label="winking tongue emoji"></span>Funny Emoji</div>
<div class="card on" style="left:613px;top:1961px"><span class="glyph lg" role="img" aria-label="magnifier emoji"></span>Search Emoji</div>
<div class="card" style="left:807px;top:1961px"><span class="glyph lg" role="img" aria-label="sunglasses emoji"></span>Smart Emoji</div>
<div class="card" style="left:225px;top:2167px"><span class="glyph lg" role="img" aria-label="smirking emoji"></span>Smart Emoji</div>
<div class="card" style="left:419px;top:2167px"><span class="glyph lg" role="img" aria-label="sad emoji"></span>So Sad Emoji</div>
<div class="card" style="left:613px;top:2167px"><span class="glyph lg" role="img" aria-label="kissing emoji"></span>Peck Emoji</div>
<div class="card" style="left:807px;top:2167px"><span class="glyph lg" role="img" aria-label="tongue emoji"></span>Fooled You Emoji</div>
<div class="card" style="left:225px;top:2372px"><span class="glyph lg" role="img" aria-label="surprised emoji"></span>Ohhh Emoji</div>
<div class="card" style="left:419px;top:2372px"><span class="glyph lg" role="img" aria-label="laughing emoji"></span>Hahah Emoji</div>
<div class="card" style="left:613px;top:2372px"><span class="glyph lg" role="img" aria-label="disappointed emoji"></span>Sad Emoji</div>
<div class="card" style="left:807px;top:2372px"><span class="glyph lg" role="img" aria-label="worried emoji"></span>Nervous Emoji</div>

<h2 class="sec" style="top:2589px"><span class="glyph" style="background:#e8553e" role="img" aria-label="umbrella emoji"></span>Related Themes &amp; <span class="accent">Holidays</span></h2>
<div class="chip" style="left:225px;top:2667px"><span class="t"><span class="glyph sm" style="background:#e8553e" role="img" aria-label="party emoji"></span>Birthday Bash</span><span class="cp"><svg viewBox="0 0 20 20"><use href="#copy"/></svg></span></div>
<div class="chip" style="left:481px;top:2667px"><span class="t"><span class="glyph sm" style="background:#e66" role="img" aria-label="holiday emoji"></span>Merry Christmas</span><span class="cp"><svg viewBox="0 0 20 20"><use href="#copy"/></svg></span></div>
<div class="chip" style="left:738px;top:2667px"><span class="t"><span class="glyph sm" style="background:#f08a24" role="img" aria-label="pumpkin emoji"></span>Halloween</span><span class="cp"><svg viewBox="0 0 20 20"><use href="#copy"/></svg></span></div>

<h2 class="sec" style="top:2764px"><span class="glyph tone" role="img" aria-label="hand emoji"></span>General Information about Painter Emoji With <span class="accent">Palette</span></h2>
<div class="abs info">
  <div class="k">
    <div class="row">Full Name</div><div class="row">Category</div><div class="row">Subcategory</div><div class="row">How to type shortcode</div><div class="row">Unicode (fully-qualified)</div><div class="row">Unicode version</div><div class="row">Listed in</div><div class="row">Hex Code Points</div><div class="row">URL Escape Code</div>
  </div>
  <div class="v">
    <div class="row"><span class="glyph tone sm" role="img" aria-label="painter emoji"></span>Painter Face With Palette</div>
    <div class="row"><span class="glyph tone sm" role="img" aria-label="painter emoji"></span>Painting</div>
    <div class="row"><span class="glyph tone sm" role="img" aria-label="painter emoji"></span>Art</div>
    <div class="row"><span class="code">:dummy_code: <svg width="18" height="18" viewBox="0 0 20 20"><rect x="5" y="2" width="11" height="14" rx="1.5" fill="none" stroke="#666" stroke-width="1.6"/><rect x="2" y="5" width="11" height="14" rx="1.5" fill="#e4e4e4" stroke="#666" stroke-width="1.6"/></svg></span></div>
    <div class="row">U+1F605</div><div class="row">Unicode 6.0 (2010)</div><div class="row">Emoji Version 2.0</div><div class="row">1F605B</div><div class="row">%F0%9F%98%85</div>
  </div>
</div>

<h2 class="sec" style="top:3393px"><span class="glyph" role="img" aria-label="nerd emoji"></span>Translations and Keywords for <span class="glyph tone sm" role="img" aria-label="painter emoji"></span> Painter Emoji With <span class="accent">Palette</span></h2>
<div class="abs trans">
  <span class="div"></span>
  <span class="k" style="top:72px">Another names, keywords</span>
  <span class="kw" style="top:72px"><span class="glyph sm" role="img" aria-label="emoji"></span>Dummy Text</span>
  <span class="kw" style="top:101px"><span class="glyph sm" role="img" aria-label="emoji"></span>Dummy Text</span>
  <span class="kw" style="top:130px"><span class="glyph sm" role="img" aria-label="emoji"></span>Dummy Text</span>
  <span class="kw" style="top:159px"><span class="glyph sm" role="img" aria-label="emoji"></span>Dummy Text</span>
  <span class="kw" style="top:188px"><span class="glyph sm" role="img" aria-label="emoji"></span>Dummy Text</span>
  <span class="k" style="top:232px">Spanish</span><span class="v" style="top:232px">Lorem ipsum dolor sit amet, consectetur</span>
  <span class="k" style="top:285px">Italian</span><span class="v" style="top:285px">Lorem ipsum dolor sit amet, consectetur</span>
  <span class="k" style="top:338px">Rusian</span><span class="v" style="top:338px">Lorem ipsum dolor sit amet, consectetur</span>
  <span class="k" style="top:391px">German</span><span class="v" style="top:391px">Lorem ipsum dolor sit amet, consectetur</span>
  <span class="k" style="top:444px">French</span><span class="v" style="top:444px">Lorem ipsum dolor sit amet, consectetur</span>
  <span class="k" style="top:497px">Portugese</span><span class="v" style="top:497px">Lorem ipsum dolor sit amet, consectetur</span>
</div>

<footer class="abs site-footer">
  <div class="flogo">LOGO</div>
  <div class="tag">Lorem Ipsum is simply dummy text of the printing and typesetting industry.</div>
  <div class="social"><span></span><span></span><span></span></div>
  <div class="bottom">Copyright © Emoji Directory | All Rights Deserved | Privacy Policy | Contact Us</div>
</footer>

</body>
</html>
```